Almadraba Holding Partners - 2018 Website

We are an investment platform based in Madrid, Spain, that focuses on buying companies to improve them operationally and ignite growth through modernization, digitalization and a real hands on approach in the management of those companies we buy. We want to become a serious player in the private equity and money management industry and start approaching more institutional investors (such as pension funds, large family offices, etc.) in the coming months for an intense fundraising campaign.

For such purpose, we need a professional website with an impeccable design and streamlined communication. While we do want to provide some details in terms of what we do, who we are, our investment strategy, etc. we also want to be as vague as possible so that we do not limit ourselves to the claims we do on the website in terms of kind of investments, sectors, industries, geographies, etc. that we work on. For now we raise capital on a deal by deal basis, although our goal is to raise a discretionary pool of capital that we would deploy over 3-5 years. We are now building our track record as a team with already 2 investments which are showing massive growth potential and for which we have been able to execute the investment thesis as planned so far.

We need a simple and clear website with an incredibly professional image to go on the above mentioned roadshow and meet institutional investors.

For reference, we believe the following investment funds have very nice websites:

1) Tordesa Private Equity - http://tordesaequity-example.com/
2) Valdemora Capital - http://www.valdemoracapital-example.es/
3) Quintela Capital - https://www.quintelacapital-example.com/

Thank you in advance.
Tomás Ibáñez Cuesta

Target Market(s)

Potential professional investors - from High Net Worth individuals, to more institutional investors such as Family Offices, Investment Funds, Pension Funds, etc.

Contact Information for Business Card

Name
Title
Contact Details (only for Rafael Sanz Úbeda and Tomás Ibáñez Cuesta)

Coding

Coded - Design and coding required

Number of Pages Required

5+ page

Font styles to use
Sans Serif

Colors

Designer to choose colors to be used in the design.

```html
<!DOCTYPE html>
<html lang="en">
<head>
<meta charset="utf-8">
<title>Almadraba Holding Partners</title>
<link rel="stylesheet" href="https://fonts.googleapis.com/css2?family=Open+Sans:wdth,wght@75..100,400..700&display=swap">
<style>
  :root {
    --navy: #2e2d4f;
    --logo-grey: #47465e;
    --text: #4a4a4a;
    --rule: #c9c9cf;
    --frame: #e4e4e6;
    --white: #ffffff;
  }
  * { margin: 0; padding: 0; box-sizing: border-box; }
  html, body { width: 1191px; height: 1200px; overflow: hidden; }
  body {
    background: var(--frame);
    font-family: "Open Sans", Arial, sans-serif;
    color: var(--text);
    position: relative;
  }
  .page {
    position: absolute;
    left: 15px; top: 15px;
    width: 1161px; height: 1170px;
    background: var(--white);
  }
  .info-bar {
    position: absolute;
    left: 650px; top: 0;
    width: 487px; height: 35px;
  }
  .info-bar svg { position: absolute; inset: 0; }
  .info-bar__content {
    position: absolute; inset: 0;
    display: flex; align-items: center; justify-content: center; gap: 8px;
    color: var(--white);
    font-weight: 700; font-size: 15px; font-stretch: 90%;
    letter-spacing: 0.2px;
  }
  .social { display: flex; gap: 4px; margin-left: 8px; }
  .social span {
    width: 19px; height: 19px; border-radius: 50%;
    border: 1.5px solid var(--white);
  }
  .brand {
    position: absolute;
    display: flex; align-items: center; gap: 14px;
    color: var(--logo-grey);
    font-weight: 400;
  }
  .brand__dot {
    width: 46px; height: 46px; border-radius: 50%;
    background: var(--navy);
    flex: none;
  }
  .brand__name {
    font-size: 25px; line-height: 1.15; letter-spacing: 2.5px;
    text-transform: uppercase;
  }
  .brand--header { left: 22px; top: 30px; }
  .nav {
    position: absolute;
    right: 55px; top: 80px;
    display: flex; align-items: center; gap: 22px;
    list-style: none;
    font-weight: 700; font-size: 16px; font-stretch: 78%;
    color: #1d1d2a;
  }
  .nav__item--active { border-bottom: 3px solid var(--navy); padding-bottom: 2px; }
  .nav__cta {
    background: var(--navy); color: var(--white);
    padding: 6px 16px; border-radius: 3px;
  }
  .hero {
    position: absolute;
    left: 0; top: 127px;
    width: 1161px; height: 550px;
    background: linear-gradient(100deg, #5a4e44 0%, #8c8275 22%, #c9c6c4 45%, #e3dfd8 55%, #b3a48f 75%, #6e6356 100%);
    box-shadow: 0 12px 14px -8px rgba(0,0,0,0.35);
  }
  .intro {
    position: absolute;
    left: 72px; top: 735px; width: 1020px;
    text-align: center;
  }
  .intro__title {
    display: flex; align-items: center; justify-content: center; gap: 22px;
    color: var(--navy);
    font-size: 25px; font-weight: 600; letter-spacing: 0.3px;
  }
  .intro__title::before, .intro__title::after {
    content: ""; width: 90px; height: 1px; background: var(--rule);
  }
  .intro__text {
    margin-top: 40px;
    font-size: 12.6px; line-height: 19.6px;
  }
  .brand--footer { left: 433px; top: 1007px; }
  .footer {
    position: absolute;
    left: 0; bottom: 0; width: 100%; height: 49px;
    border-top: 1px solid #8a8a8a;
    display: flex; align-items: center; justify-content: center;
    font-size: 11.5px; font-weight: 700; color: #333;
  }
</style>
</head>
<body>
<div class="page">
  <div class="info-bar">
    <svg width="487" height="35" viewBox="0 0 487 35" aria-hidden="true">
      <polygon points="0,0 487,0 462,35 25,35" fill="var(--navy)"/>
    </svg>
    <div class="info-bar__content">
      <svg width="20" height="20" viewBox="0 0 20 20" aria-hidden="true">
        <circle cx="10" cy="10" r="9" fill="none" stroke="#fff" stroke-width="1.5"/>
        <path d="M6.5 5.5l2 2-1 1.2c.6 1.4 1.6 2.4 3 3l1.2-1 2 2-1.2 1.4c-3-.4-6.2-3.6-6.6-6.6z" fill="#fff"/>
      </svg>
      <span>FOR INFORMATION : +34 91 000 48 21</span>
      <span class="social" aria-label="Social links"><span></span><span></span><span></span></span>
    </div>
  </div>

  <div class="brand brand--header">
    <span class="brand__dot"></span>
    <span class="brand__name">Almadraba<br>Holding Partners</span>
  </div>

  <ul class="nav">
    <li class="nav__item nav__item--active">HOME</li>
    <li class="nav__item">ABOUT</li>
    <li class="nav__item">SERVICES</li>
    <li class="nav__item">NEWS</li>
    <li class="nav__item nav__cta">CONTACT US</li>
  </ul>

  <div class="hero" role="img" aria-label="Photograph of a historic city street lined with classical stone government buildings under a cloudy sky"></div>

  <section class="intro">
    <h1 class="intro__title">ALMADRABA HOLDING PARTNERS</h1>
    <p class="intro__text">Lorem ipsum dolor sit amet, consectetuer adipiscing elit, sed diam nonummy nibh euismod tincidunt ut laoreet dolore magna aliquam erat volutpat. Ut wisi enim ad minim veniam, quis nostrud exerci tation ullamcorper suscipit lobortis nisl ut aliquip ex ea commodo consequat. Duis autem vel eum iriure dolor in hendrerit in vulputate velit esse molestie consequat, vel illum dolore eu feugiat nulla facilisis at vero eros et accumsan et iusto odio dignissim qui blandit praesent luptatum zzril delenit augue duis dolore te feugait nulla facilisi. Nam liber tempor cum soluta nobis eleifend option congue nihil imperdiet doming id quod mazim placerat facer possim assum. Typi non habent claritatem insitam; est usus legentis in iis qui facit eorum claritatem. Investigationes demonstraverunt lectores legere me lius quod ii legunt saepius.</p>
  </section>

  <div class="brand brand--footer">
    <span class="brand__dot"></span>
    <span class="brand__name">Almadraba<br>Holding Partners</span>
  </div>

  <footer class="footer">© 2018 ALMADRABA HOLDING PARTNERS I ALL RIGHTS RESERVED</footer>
</div>
</body>
</html>
```